BRYLTAllies.co.uk - Mental Health Clinic for Child and Adolescents

Updated 29/01/2018***
I am not sure you guys are getting the idea regards to the opening page / homescreen layout. Can you look at the new images I have uploaded (page 5, 6 and 7) These are some of the layouts I like but to incorporate my chosen images, with the BRYLT commissioner, buttons and a sliding header bar.
I have written a strong brief, I am looking for a website, preferably wordpress as i know they are easy to maintain. I am looking for a one page site, with the top / opening page being full screen image with drop down categories. I have made a rough design, see full brief in word doc attached, there is some freedom to play around with the design aspect but it will need to relay all the content provided. I like a minimal feel. I have also attached some images that may be useful, but will need a new logo for BRYLT Allies. I have attached some logo idea's, it is up to you decide whether you want to use them.
I would prefer the homepage as full screen image, and the categories offered as a drop down or over the main image.
I have also attached linked to some competitors websites:
https://www.verdano-group.co.uk/
http://www.qwmr.org.uk/
Industry/Entity Type
Clinic
Number of Pages Required
1 page
Font styles to use
Look and feel
Each slider illustrates characteristics of the customer's brand and the style your logo design should communicate.

```html
<!DOCTYPE html>
<html lang="en">
<head>
<meta charset="utf-8">
<title>BRYLT Allies – Child &amp; Adolescent Mental Health Services</title>
<link href="https://fonts.googleapis.com/css2?family=Open+Sans:wght@400;600;700&family=Montserrat:wght@500;600&display=swap" rel="stylesheet">
<style>
  :root{
    --sidebar:#26343a;
    --sidebar-line:#33444b;
    --sidebar-text:#e9eef0;
    --brand:#f2e21c;
    --accent:#3fe0ea;
    --ink:#2b2b2b;
    --muted:#9a9a9a;
    --panel:#e7e7e7;
    --card:#ffffff;
    --hero-top:#dedcd8;
    --hero-mid:#8f9897;
    --hero-bottom:#2f3f44;
  }
  *{box-sizing:border-box;margin:0;padding:0}
  html,body{width:1200px;height:1200px;overflow:hidden;background:#fff}
  body{font-family:"Open Sans",Arial,sans-serif;color:var(--ink);position:relative}

  /* Sidebar */
  .sidebar{position:absolute;left:0;top:0;width:200px;height:1200px;background:var(--sidebar);color:var(--sidebar-text)}
  .sidebar__brand{height:118px;background:#1f2c31;display:flex;align-items:center;gap:10px;padding:0 14px}
  .brand-dot{width:38px;height:38px;border-radius:50%;background:var(--brand);flex:none}
  .brand-name{font-weight:700;font-size:26px;color:var(--brand);line-height:1}
  .brand-sub{font-size:7.5px;color:#fff;line-height:1.2;margin-top:3px}
  .nav{list-style:none;padding:18px 22px 0 22px}
  .nav li{font-size:10px;font-weight:600;text-transform:uppercase;padding:9px 0 8px;border-bottom:1px solid var(--sidebar-line);display:flex;justify-content:space-between}
  .sidebar__social{position:absolute;left:0;right:0;top:470px;display:flex;justify-content:center;gap:3px}
  .sidebar__social span{width:14px;height:14px;border-radius:50%;background:#cfd6d8}
  .sidebar__footer{position:absolute;left:0;right:0;top:498px;height:26px;border-top:1px solid var(--sidebar-line);font-size:7px;font-weight:600;text-transform:uppercase;text-align:center;line-height:26px}

  /* Hero */
  .hero{position:absolute;left:200px;top:0;width:1000px;height:540px;overflow:hidden}
  .hero__photo{position:absolute;inset:0;background:linear-gradient(180deg,var(--hero-top) 0%,#b9b3a8 45%,var(--hero-mid) 70%,var(--hero-bottom) 100%)}
  .hero__contact{position:absolute;top:16px;right:16px;font-size:9px;color:#fff}
  .hero__logo{position:absolute;left:290px;top:18px;display:flex;align-items:center;gap:14px}
  .hero__logo .brand-dot{width:96px;height:96px}
  .hero__logo .brand-name{font-size:52px}
  .hero__logo .brand-sub{font-size:15px;color:#6b6b6b;margin-top:6px;font-weight:400}
  .pill{position:absolute;top:305px;width:210px;height:52px;border-radius:26px;background:rgba(255,255,255,.78);font-family:"Montserrat",sans-serif;font-weight:600;font-size:17px;letter-spacing:.5px;color:#2d3a3f;display:flex;align-items:center;justify-content:center}
  .pill--parents{left:190px}
  .pill--commissioners{left:540px}
  .hero__quote{position:absolute;top:440px;left:0;right:0;text-align:center;color:#fff;font-size:27px;line-height:1.28}
  .hero__dots{position:absolute;top:514px;left:0;right:0;display:flex;justify-content:center;gap:8px}
  .hero__dots span{width:6px;height:6px;border-radius:50%;background:#fff}

  /* About */
  .about{position:absolute;left:200px;top:540px;width:1000px;height:240px;overflow:hidden}
  .about__photo{position:absolute;inset:0;background:linear-gradient(90deg,#ede6e3 0%,#f7f1ef 45%,#f3e8e8 100%)}
  .about__text{position:absolute;left:120px;width:760px;top:38px;text-align:center;font-size:11.5px;line-height:24px;color:#333}
  .about__text b{font-weight:700}
  .btn-contact{position:absolute;left:400px;top:180px;width:196px;height:42px;border-radius:21px;background:var(--accent);color:#fff;font-weight:700;font-size:14px;display:flex;align-items:center;justify-content:center}

  /* Team */
  .team{position:absolute;left:200px;top:780px;width:1000px;height:420px;background:var(--panel)}
  .team__title{text-align:center;font-size:24px;font-weight:400;margin-top:30px;letter-spacing:.5px}
  .team__title span{color:var(--accent)}
  .team__intro{width:680px;margin:14px auto 0;text-align:center;font-size:11px;line-height:24px}
  .team__grid{position:absolute;left:102px;top:150px;display:grid;grid-template-columns:336px 336px;column-gap:34px;row-gap:30px}
  .card{background:var(--card);border-radius:4px;height:120px;display:flex;padding:7px;gap:12px}
  .card__photo{width:128px;height:106px;flex:none;background:linear-gradient(180deg,#dcdcdc,#9c9c9c)}
  .card__name{font-weight:700;font-size:14px;margin-top:2px}
  .card__role{font-size:7.5px;color:var(--muted);text-transform:uppercase;font-weight:600}
  .card__bio{font-size:8px;line-height:10.5px;margin-top:9px;width:160px}
  .card__social{display:flex;gap:4px;margin-top:7px}
  .card__social span{width:14px;height:14px;border-radius:50%;border:1.5px solid var(--accent)}
</style>
</head>
<body>

<aside class="sidebar">
  <div class="sidebar__brand">
    <span class="brand-dot"></span>
    <div>
      <div class="brand-name">BRYLT</div>
      <div class="brand-sub">Child &amp; Adolescent Mental<br>Health Services</div>
    </div>
  </div>
  <ul class="nav">
    <li>About Us</li>
    <li>The Team</li>
    <li>Parents</li>
    <li>Commissioners</li>
    <li>Our Services <svg width="8" height="10" viewBox="0 0 8 10"><path d="M2 1l4 4-4 4" fill="none" stroke="#e9eef0" stroke-width="1.4"/></svg></li>
    <li>Blog</li>
    <li>Forum</li>
    <li>Contact Us</li>
  </ul>
  <div class="sidebar__social"><span></span><span></span><span></span><span></span><span></span></div>
  <div class="sidebar__footer">About BRYLT Allies</div>
</aside>

<section class="hero">
  <div class="hero__photo" role="img" aria-label="Five smiling young people sitting together on a teal sofa in front of a white brick wall"></div>
  <div class="hero__contact">
    <svg width="11" height="8" viewBox="0 0 11 8" style="vertical-align:middle"><rect x=".5" y=".5" width="10" height="7" fill="none" stroke="#fff"/><path d="M.5 .5l5 4 5-4" fill="none" stroke="#fff"/></svg>
    info@BRYLTAllies.co.uk &nbsp;|&nbsp;
    <svg width="9" height="9" viewBox="0 0 10 10" style="vertical-align:middle"><path d="M2 1l2 2-1 1.5c.7 1.3 1.6 2.2 2.5 2.5L7 6l2 2-1.5 1.5C4 9 1 6 .5 2.5z" fill="#fff"/></svg>
    (+44) 100 555 0199
  </div>
  <div class="hero__logo">
    <span class="brand-dot"></span>
    <div>
      <div class="brand-name">BRYLT</div>
      <div class="brand-sub">Child &amp; Adolescent Mental<br>Health Services</div>
    </div>
  </div>
  <div class="pill pill--parents">PARENTS</div>
  <div class="pill pill--commissioners">COMMISIONERS</div>
  <p class="hero__quote">“ADHD and Autism Screening<br>withing 24 hours”</p>
  <div class="hero__dots"><span></span><span></span></div>
</section>

<section class="about">
  <div class="about__photo" role="img" aria-label="Soft faded photo of a young person talking with a clinician"></div>
  <p class="about__text"><b>BRYLT ALLIES</b> offer the best BRYLT assessments, therapy and aftercare. We have a unique model that allows families to be seen quickly by handpicked clinicians that are highly skilled and experienced. We offer a turnaround time of 24 hours for all ADHD and ASD screening, and aim to complete a full assessment within 14 days. If your child has been diagnosed we offer post diagnosis support to both the child and family.</p>
  <div class="btn-contact">CONTACT US!</div>
</section>

<section class="team">
  <h2 class="team__title">THE <span>TEAM</span></h2>
  <p class="team__intro"><b>THE TEAM</b> at BRYLT are professional and passion driven individuals who help children and adolescent with disorder for proper consultation and diagnostic. They make a difference for people.</p>
  <div class="team__grid">
    <article class="card">
      <div class="card__photo" role="img" aria-label="Portrait photo of a team member"></div>
      <div>
        <div class="card__name">LOREM IPSUM</div>
        <div class="card__role">President &amp; Co-Founder</div>
        <p class="card__bio">Lorem ipsum dolor sit amet, consectetur adipiscing elit. Cras sed felis tempor, dictum diam non, egestas sapien. Nulla vitae sem gravida, imperdiet nisl sed, luctus nisl.</p>
        <div class="card__social"><span></span><span></span><span></span><span></span></div>
      </div>
    </article>
    <article class="card">
      <div class="card__photo" role="img" aria-label="Portrait photo of a team member"></div>
      <div>
        <div class="card__name">LOREM IPSUM</div>
        <div class="card__role">Co-Founder</div>
        <p class="card__bio">Lorem ipsum dolor sit amet, consectetur adipiscing elit. Cras sed felis tempor, dictum diam non, egestas sapien. Nulla vitae sem gravida, imperdiet nisl sed, luctus nisl.</p>
        <div class="card__social"><span></span><span></span><span></span><span></span></div>
      </div>
    </article>
    <article class="card">
      <div class="card__photo" role="img" aria-label="Portrait photo of a team member"></div>
      <div>
        <div class="card__name">LOREM IPSUM</div>
        <div class="card__role">President &amp; Co-Founder</div>
        <p class="card__bio">Lorem ipsum dolor sit amet, consectetur adipiscing elit. Cras sed felis tempor, dictum diam non, egestas sapien. Nulla vitae sem gravida, imperdiet nisl sed, luctus nisl.</p>
        <div class="card__social"><span></span><span></span><span></span><span></span></div>
      </div>
    </article>
    <article class="card">
      <div class="card__photo" role="img" aria-label="Portrait photo of a team member"></div>
      <div>
        <div class="card__name">LOREM IPSUM</div>
        <div class="card__role">Co-Founder</div>
        <p class="card__bio">Lorem ipsum dolor sit amet, consectetur adipiscing elit. Cras sed felis tempor, dictum diam non, egestas sapien. Nulla vitae sem gravida, imperdiet nisl sed, luctus nisl.</p>
        <div class="card__social"><span></span><span></span><span></span><span></span></div>
      </div>
    </article>
  </div>
</section>

</body>
</html>
```